Offer banner redesign / Simplifying existing banner

We have a banner there customer can click on to get an offer. We want to simplify this banner and to get it to at minimum. We are not clear about how it shoulderstand look like, but the actual banner you can see here (It's at the top of the page): https://ofenrohr-lagerhaus.de/kaminsysteme/ We want to get rid of the icons and to reduce the size of the baner. The baner shoulderstand contain the Following text: Affordable chimney using installation service button text: Request free quote

Target Market(s)

Customers from age of 40yrs.

Requirements
Must have
• Clear and good visible button
Nice to have
• It Should be simple and striking.

```html
<!DOCTYPE html>
<html lang="en">
<head>
<meta charset="UTF-8">
<title>Offer Banner – Chimney Installation</title>
<link rel="stylesheet" href="https://fonts.googleapis.com/css2?family=Arimo:wght@700&family=Noto+Sans:wght@700&display=swap">
<style>
  :root {
    --canvas: #ffffff;
    --band: #f3f3f3;
    --ink: #111111;
    --accent: #f4ae36;
    --button-edge: #c9c3b6;
  }
  html, body {
    margin: 0;
    padding: 0;
    width: 1200px;
    height: 1200px;
    overflow: hidden;
    background: var(--canvas);
  }
  .canvas {
    position: relative;
    width: 1200px;
    height: 1200px;
  }
  .offer-banner {
    position: absolute;
    left: 19px;
    width: 1162px;
    height: 143px;
    background: var(--band);
    text-align: center;
  }
  .offer-banner--dark { top: 404px; }
  .offer-banner--accent { top: 650px; }
  .offer-title {
    margin: 0;
    padding-top: 14px;
    font-family: "Arimo", Arial, sans-serif;
    font-weight: 700;
    font-size: 32px;
    line-height: 40px;
    letter-spacing: 0.5px;
    white-space: nowrap;
    color: var(--ink);
  }
  .offer-banner--accent .offer-title { color: var(--accent); }
  .offer-button {
    display: inline-block;
    box-sizing: border-box;
    margin-top: 17px;
    width: 282px;
    height: 59px;
    line-height: 55px;
    background: var(--accent);
    border: 2px solid var(--button-edge);
    border-radius: 4px;
    font-family: "Noto Sans", Verdana, sans-serif;
    font-weight: 700;
    font-size: 21px;
    letter-spacing: 1px;
    white-space: nowrap;
    color: var(--ink);
    text-decoration: none;
  }
</style>
</head>
<body>
  <main class="canvas">
    <section class="offer-banner offer-banner--dark">
      <h2 class="offer-title">AFFORDABLE CHIMNEY USING INSTALLATION SERVICE</h2>
      <a class="offer-button" href="#request-quote">REQUEST FREE QUOTE</a>
    </section>
    <section class="offer-banner offer-banner--accent">
      <h2 class="offer-title">AFFORDABLE CHIMNEY USING INSTALLATION SERVICE</h2>
      <a class="offer-button" href="#request-quote">REQUEST FREE QUOTE</a>
    </section>
  </main>
</body>
</html>
```